Aviation Banner Ad Designs

SkyLedgerMetrics provides access to the most accurate aircraft operating cost information, to compare Piston, Turboprop and Jet aircraft.

The banners ads will be used for retargeting/remarketing - to bring visitors back to the site. The banners should remind and reinforce the key messages of what the site provides.

Target Market(s)

Private aircraft buyers including:
- Aircraft Brokers
- Charter Operators
- Corporate Flight Departments
- Aircraft Management companies
- Financial Institutions
- Aircraft Owners
- Prospective Buyers

Requirements
Must have
• A. Banner Objective
The visual and textual content of the banner should remind the viewer about the features of the site, and prompt them to return to the site.
1. Arresting visual
2. Headline
3. Single message
4. Compelling CTA
5. Logo - big enough to see
6. Standard IAB ad sizes/specs

B. Design Elements
Logo: As attached
Main Title: Calculate Jet Operating Costs
Subtitle: Compare Ownership Usage Scenarios
Call to Action Button: Compare Ownership Costs
Background: Several images supplied as options

C. Banner Sizes
Do examples as 300×250 , 728×90 , 160×600
Final sizes to also include 320×100 , 336x280 , 300x600

Finally delivery as .jpg files.

Font - use same font as on site

```html
<!DOCTYPE html>
<html lang="en">
<head>
<meta charset="utf-8">
<title>SkyLedgerMetrics – Banner Set</title>
<link rel="stylesheet" href="https://fonts.googleapis.com/css2?family=Arimo:wght@400;700&display=swap">
<style>
  :root {
    --page-bg: #eceef0;
    --white: #ffffff;
    --ink: #1a1a1a;
    --teal: #2b86a6;
    --red: #d9404a;
    --band-dark: rgba(58, 60, 64, 0.86);
    --band-mid: rgba(70, 74, 82, 0.82);
    --sky-top: #c9d3e6;
    --sky-bottom: #7f93b4;
    --mark-red: #d62b32;
  }
  * { box-sizing: border-box; margin: 0; padding: 0; }
  html, body { width: 1200px; height: 720px; overflow: hidden; }
  body {
    background: var(--page-bg);
    font-family: "Arimo", Arial, sans-serif;
    position: relative;
  }
  .banner {
    position: absolute;
    overflow: hidden;
    box-shadow: 0 3px 10px rgba(0,0,0,0.18);
    color: var(--white);
  }
  .photo { position: absolute; inset: 0; }
  .brand {
    position: absolute;
    display: flex;
    align-items: center;
    gap: 7px;
    color: var(--ink);
    font-weight: 700;
    white-space: nowrap;
  }
  .brand-square { background: var(--mark-red); display: block; flex: none; }
  .cta {
    position: absolute;
    display: flex;
    align-items: center;
    justify-content: center;
    font-weight: 700;
    color: var(--white);
    text-align: center;
  }

  /* 728 x 90 leaderboard */
  .leaderboard { left: 40px; top: 50px; width: 728px; height: 90px; }
  .leaderboard .photo {
    background: linear-gradient(90deg, #ececec 0%, #d9d7d4 32%, #8f8a84 52%, #6b5a4a 72%, #4a3b31 100%);
  }
  .leaderboard .brand { left: 20px; top: 30px; font-size: 22px; }
  .leaderboard .brand-square { width: 26px; height: 26px; }
  .leaderboard .headline {
    position: absolute; right: 17px; top: 3px;
    font-size: 25px; font-weight: 700; letter-spacing: -0.3px;
    text-shadow: 0 1px 2px rgba(0,0,0,0.35);
  }
  .leaderboard .subhead {
    position: absolute; right: 17px; top: 31px;
    font-size: 17px;
    text-shadow: 0 1px 2px rgba(0,0,0,0.35);
  }
  .leaderboard .cta {
    right: 0; bottom: 0; width: 242px; height: 32px;
    background: var(--teal); font-size: 17px;
  }

  /* 300 x 250 medium rectangle */
  .rectangle { left: 40px; top: 190px; width: 300px; height: 250px; }
  .rectangle .photo {
    background: linear-gradient(170deg, #c4c6c9 0%, #9ea1a6 35%, #7f7c79 60%, #b3aea8 85%, #d3d0cb 100%);
  }
  .rectangle .brand { right: 16px; top: 22px; font-size: 19px; }
  .rectangle .brand-square { width: 22px; height: 22px; }
  .rectangle .message {
    position: absolute; left: 0; top: 72px; width: 300px; height: 76px;
    background: var(--band-dark);
    text-align: center; padding-top: 12px;
  }
  .rectangle .headline { font-size: 20px; font-weight: 700; letter-spacing: -0.3px; }
  .rectangle .subhead { font-size: 15px; margin-top: 6px; }
  .rectangle .cta {
    left: 0; top: 172px; width: 210px; height: 48px;
    background: var(--red); font-size: 16px;
  }

  /* 160 x 600 wide skyscraper */
  .skyscraper { left: 1000px; top: 50px; width: 160px; height: 600px; }
  .skyscraper .sky {
    position: absolute; left: 0; top: 0; width: 160px; height: 264px;
    background: linear-gradient(180deg, #f1f2f5 0%, var(--sky-top) 30%, var(--sky-bottom) 100%);
  }
  .skyscraper .brand { left: 8px; top: 44px; font-size: 15px; gap: 5px; }
  .skyscraper .brand-square { width: 16px; height: 16px; }
  .skyscraper .headline {
    position: absolute; left: 0; top: 160px; width: 160px;
    text-align: center; font-size: 24px; font-weight: 700;
    line-height: 30px; letter-spacing: -0.3px;
  }
  .skyscraper .message {
    position: absolute; left: 0; top: 264px; width: 160px; height: 66px;
    background: #5a5e66;
    display: flex; align-items: center; justify-content: center;
    text-align: center; font-size: 14px; line-height: 19px;
  }
  .skyscraper .photo {
    top: 330px; height: 270px;
    background: linear-gradient(180deg, #7ea3cf 0%, #b5c6da 30%, #e3e6ea 55%, #2f3c52 85%, #1f2a3c 100%);
  }
  .skyscraper .cta {
    left: 0; top: 460px; width: 160px; height: 78px;
    background: var(--red); font-size: 20px; font-weight: 400; line-height: 25px;
  }
</style>
</head>
<body>

  <section class="banner leaderboard" aria-label="728 by 90 banner">
    <div class="photo" role="img" aria-label="Business jet taking off against a warm sunset sky"></div>
    <div class="brand"><span class="brand-square"></span>SkyLedgerMetrics</div>
    <h1 class="headline">Calculate Jet Operating Costs</h1>
    <p class="subhead">Compare Ownership Usage Scenarios</p>
    <div class="cta">Compare Ownership Costs</div>
  </section>

  <section class="banner rectangle" aria-label="300 by 250 banner">
    <div class="photo" role="img" aria-label="Close view of a parked business jet fuselage and boarding stairs"></div>
    <div class="brand"><span class="brand-square"></span>SkyLedgerMetrics</div>
    <div class="message">
      <h2 class="headline">Calculate Jet Operating Costs</h2>
      <p class="subhead">Compare Ownership Usage Scenarios</p>
    </div>
    <div class="cta">Compare Ownership Costs</div>
  </section>

  <section class="banner skyscraper" aria-label="160 by 600 banner">
    <div class="sky"></div>
    <div class="brand"><span class="brand-square"></span>SkyLedgerMetrics</div>
    <h2 class="headline">Calculate Jet<br>Operating<br>Costs</h2>
    <p class="message">Compare Ownership<br>Usage Scenarios</p>
    <div class="photo" role="img" aria-label="Business jet cockpit nose under a blue sky with clouds"></div>
    <div class="cta">Compare<br>Ownership<br>Costs</div>
  </section>

</body>
</html>
```